Accommodation business card design

We need a business card designed for our long-term accommodation business based in Australia. The business card must match the style of the attached letterhead and logo. The same contact details that are on the letterhead will also go on the card except that the card must list the contact details in the following order:phone, email, home address, ABN.

The card will be printed on .76mm white pvc plastic (same as credit cards), printed both sides and will be silver foil stamped on at least one side (preferably 2 sides) The design template is attached, but please go to www.zt.com.au for more specs.

The only other addition the card will be my name: Malcolm Darby

```html
<!DOCTYPE html>
<html lang="en">
<head>
<meta charset="utf-8">
<title>Summit Lodging – Business Card</title>
<link href="https://fonts.googleapis.com/css2?family=Open+Sans:wght@400;600;700&display=swap" rel="stylesheet">
<style>
  :root {
    --maroon: #6e1f22;
    --maroon-deep: #4e1214;
    --maroon-light: #8a2c2c;
    --white: #ffffff;
    --ink: #4a4a4a;
    --icon: #7a7a7a;
    --backdrop: #ecebe9;
  }
  * { margin: 0; padding: 0; box-sizing: border-box; }
  html, body { width: 1200px; height: 1200px; overflow: hidden; }
  body {
    background: var(--backdrop);
    font-family: "Open Sans", Arial, sans-serif;
    display: flex;
    flex-direction: column;
    align-items: center;
    justify-content: center;
    gap: 60px;
  }
  .card {
    position: relative;
    width: 880px;
    height: 500px;
    border-radius: 6px;
    overflow: hidden;
    box-shadow: 0 10px 30px rgba(0,0,0,0.18);
    background: var(--white);
  }
  .card-art { position: absolute; inset: 0; width: 100%; height: 100%; }

  /* Front */
  .front-brand {
    position: absolute;
    top: 138px;
    left: 0;
    width: 100%;
    display: flex;
    align-items: center;
    justify-content: center;
    gap: 16px;
  }
  .brand-square {
    width: 46px;
    height: 46px;
    background: var(--maroon);
  }
  .front-brand .brand-name {
    font-weight: 700;
    font-size: 40px;
    letter-spacing: 1px;
    color: var(--maroon);
    text-transform: uppercase;
  }

  /* Back */
  .back-brand {
    position: absolute;
    left: 48px;
    top: 222px;
    display: flex;
    align-items: center;
    gap: 14px;
  }
  .back-brand .brand-square { background: var(--white); width: 42px; height: 42px; }
  .back-brand .brand-name {
    font-weight: 700;
    font-size: 34px;
    letter-spacing: 1px;
    color: var(--white);
    text-transform: uppercase;
  }
  .holder-name {
    position: absolute;
    left: 596px;
    top: 74px;
    font-weight: 600;
    font-size: 34px;
    color: var(--maroon);
  }
  .contact-list {
    position: absolute;
    left: 556px;
    top: 180px;
    list-style: none;
    color: var(--ink);
    font-size: 16px;
    line-height: 1.3;
  }
  .contact-item {
    display: flex;
    align-items: flex-start;
    gap: 14px;
    margin-bottom: 22px;
  }
  .contact-icon { width: 22px; height: 22px; flex: none; }
  .contact-abn { padding-left: 36px; margin-top: 8px; }
</style>
</head>
<body>

  <section class="card card-front" aria-label="Card front">
    <svg class="card-art" viewBox="0 0 880 500" aria-hidden="true">
      <defs>
        <linearGradient id="frontBand" x1="0" y1="0" x2="0" y2="1">
          <stop offset="0" stop-color="#8a2c2c"/>
          <stop offset="1" stop-color="#4e1214"/>
        </linearGradient>
      </defs>
      <path d="M0,395 C260,372 600,330 880,262 L880,500 L0,500 Z" fill="url(#frontBand)"/>
      <path d="M0,395 C260,372 600,330 880,262" fill="none" stroke="#ffffff" stroke-opacity="0.35" stroke-width="3"/>
      <path d="M280,336 C520,300 720,246 880,170 L880,206 C720,268 520,312 280,336 Z" fill="#6e1f22"/>
      <path d="M340,200 C300,270 320,360 380,420" fill="none" stroke="#000" stroke-opacity="0.04" stroke-width="40"/>
    </svg>
    <div class="front-brand">
      <span class="brand-square"></span>
      <span class="brand-name">Summit Lodging</span>
    </div>
  </section>

  <section class="card card-back" aria-label="Card back">
    <svg class="card-art" viewBox="0 0 880 500" aria-hidden="true">
      <defs>
        <linearGradient id="backField" x1="0" y1="0" x2="1" y2="1">
          <stop offset="0" stop-color="#7d2626"/>
          <stop offset="1" stop-color="#4e1214"/>
        </linearGradient>
      </defs>
      <rect width="880" height="500" fill="url(#backField)"/>
      <path d="M560,0 C430,110 420,350 540,500 L880,500 L880,0 Z" fill="#5a1618"/>
      <path d="M580,0 C460,110 450,350 570,500 L880,500 L880,0 Z" fill="#ffffff"/>
      <path d="M575,40 C490,150 488,360 575,470" fill="none" stroke="#6e1f22" stroke-width="5"/>
    </svg>

    <div class="back-brand">
      <span class="brand-square"></span>
      <span class="brand-name">Summit Lodging</span>
    </div>

    <h1 class="holder-name">Malcolm Darby</h1>

    <ul class="contact-list">
      <li class="contact-item">
        <svg class="contact-icon" viewBox="0 0 22 22" aria-hidden="true">
          <circle cx="11" cy="11" r="11" fill="var(--icon)"/>
          <path d="M7,6 L9,6 L10,9 L8.6,10 C9.3,11.6 10.4,12.7 12,13.4 L13,12 L16,13 L16,15 C16,15.6 15.6,16 15,16 C10.6,16 6,11.4 6,7 C6,6.4 6.4,6 7,6 Z" fill="#fff"/>
        </svg>
        <span>0400 318 264</span>
      </li>
      <li class="contact-item">
        <svg class="contact-icon" viewBox="0 0 22 22" aria-hidden="true">
          <circle cx="11" cy="11" r="11" fill="var(--icon)"/>
          <rect x="5.5" y="7" width="11" height="8" fill="#fff"/>
          <path d="M5.5,7 L11,11.5 L16.5,7" fill="none" stroke="var(--icon)" stroke-width="1.2"/>
        </svg>
        <span>malcolm.darby@mailbox.com.au</span>
      </li>
      <li class="contact-item">
        <svg class="contact-icon" viewBox="0 0 22 22" aria-hidden="true">
          <circle cx="11" cy="11" r="11" fill="var(--icon)"/>
          <path d="M11,4.5 C8.5,4.5 6.8,6.3 6.8,8.6 C6.8,11.6 11,17 11,17 C11,17 15.2,11.6 15.2,8.6 C15.2,6.3 13.5,4.5 11,4.5 Z" fill="#fff"/>
          <circle cx="11" cy="8.7" r="1.6" fill="var(--icon)"/>
        </svg>
        <span>PO Box 1187, Harbour Mail Centre<br>QLD 4700</span>
      </li>
      <li class="contact-abn">ABN 51 804 227 316</li>
    </ul>
  </section>

</body>
</html>
```